Velmaro App for Smart Devices IoT WiFi Electronic

Velmaro is a siren manufacturer. This application is used for the company's products that have a Wi-Fi connection and an internet connection, which can be configured and activated remotely through this application. In addition, this application is used to activate the siren at specific times for the start and end of shifts in companies and schools. Users will be siren installers and IT or HR managers.
In addition to activating motorized sirens timers, some siren models have speakers and allow you to play TTS (text to speech) audio, audio recorded by the user on the phone and upload audio (mp3) with playlist programming with start and end times.
Application screens: home with dashboard (one dashboard for each category). Device categories: timers, speakers, motorized siren. Screen for requesting evaluation in the Play Store. Screen for registering the user profile. Screen for registering devices according to their category (timers, speakers, motorized siren). Screen for registering device groups. Screen for pairing the device on the client's Wi-Fi network. Screen for registering activation times. Screen for uploading MP3 audios. Screen for registering playlists with audio selection, start and end times. Screen for recording audio for later sending to the speakers. Screen for converting text to speech and sending to the speakers. It is important to have a time picker with the day of the week to program the activation times and playlist.

Target Market(s)

Schools, Companies and Stores.

Industry/Entity Type

IoT

Font styles to use
Sans Serif
Other font styles liked:
• roboto

Colors
FFC000
F8CF3A
FAE287
FDF2CF
FEFAEE

Requirements
Must have
• time picker with weekdays for timer programming feature.
Nice to have
• app review request screen on play store

```html
<!DOCTYPE html>
<html lang="en">
<head>
<meta charset="utf-8">
<title>Velmaro – Siren App Screens</title>
<link href="https://fonts.googleapis.com/css2?family=Poppins:wght@300;400;500&display=swap" rel="stylesheet">
<style>
:root{
  --backdrop:#FFEBB0;
  --panel:#FFFFFF;
  --primary:#FFC000;
  --primary-soft:#F8CF3A;
  --tint:#FDF2CF;
  --tint-light:#FEFAEE;
  --track:#E9E9E9;
  --ink:#2B2B2B;
  --ink-soft:#5E5E5E;
  --ink-muted:#8A8A8A;
  --icon:#3A3A3A;
}
*{box-sizing:border-box;margin:0;padding:0}
html,body{width:1200px;height:857px;overflow:hidden;background:var(--backdrop)}
body{font-family:'Poppins',sans-serif;color:var(--ink)}
.stage{position:relative;width:1276px;height:911px;transform:scale(0.94044);transform-origin:0 0}
.screen{position:absolute;top:34px;width:390px;height:844px;background:var(--panel);overflow:hidden}
.screen--timers{left:30px}
.screen--devices{left:443px}
.screen--schedule{left:856px}

.app-bar{position:absolute;top:40px;left:0;right:0;height:28px}
.app-bar .profile{position:absolute;left:29px;top:6px}
.app-bar .wifi{position:absolute;left:312px;top:7px}
.app-bar .menu{position:absolute;left:346px;top:7px}
.brand{position:absolute;left:0;right:0;top:-3px;text-align:center;font-size:25px;font-weight:500;color:var(--primary);letter-spacing:.3px}
.screen-title{position:absolute;top:85px;left:0;right:0;text-align:center;font-size:16px;font-weight:400;color:var(--ink-soft)}

.card{position:absolute;left:28px;width:332px;background:var(--panel);border-radius:8px;box-shadow:0 2px 6px rgba(0,0,0,.13)}
.toggle{position:absolute;width:32px;height:16px}
.toggle .track{position:absolute;left:0;top:2px;width:30px;height:14px;border-radius:7px;background:var(--track)}
.toggle .knob{position:absolute;left:15px;top:0;width:18px;height:18px;border-radius:50%;background:var(--primary)}

/* timers screen */
.shift-card{top:123px;height:83px;background:var(--tint)}
.shift-card .icon{position:absolute;left:17px;top:18px}
.shift-card .name{position:absolute;left:44px;top:20px;font-size:14px}
.shift-card .hint{position:absolute;left:44px;top:41px;font-size:13px;color:var(--ink-soft)}
.shift-card .toggle{left:280px;top:21px}
.section-head{position:absolute;left:28px;top:225px;display:flex;align-items:center;gap:7px;font-size:16px;font-weight:500;color:var(--ink-soft)}
.schedule{padding:18px 18px 0 18px}
.schedule .time{font-size:14px;line-height:20px}
.schedule .days{position:absolute;left:169px;top:22px;font-size:10px;color:var(--ink-soft)}
.schedule .label{font-size:13px;color:var(--ink-soft);margin-top:6px}
.schedule .audio{font-size:12.5px;color:var(--ink-soft);margin-top:3px}
.schedule .note{font-size:9px;color:var(--ink-muted);margin-top:2px}
.schedule .timer-icon{position:absolute;left:299px;top:20px}
.schedule .edit-icon{position:absolute;left:298px;top:48px}
.status{position:absolute;left:0;right:0;top:773px;height:71px;background:var(--tint);padding:12px 0 0 47px}
.status .dot{position:absolute;left:29px;top:16px;width:8px;height:8px;border-radius:50%;background:var(--primary)}
.status .head{font-size:12.5px}
.status .line{font-size:9.5px;color:var(--ink-soft);line-height:16px}

/* devices screen */
.device{height:61px}
.device .icon{position:absolute;left:17px;top:19px}
.device .name{position:absolute;left:44px;top:20px;font-size:14px}
.device .toggle{left:280px;top:20px}

/* schedule form */
.field-label{position:absolute;left:28px;font-size:14px;color:var(--ink)}
.input{position:absolute;left:28px;width:332px;height:37px;background:var(--panel);border-radius:8px;box-shadow:0 2px 5px rgba(0,0,0,.13);padding:0 20px;display:flex;align-items:center;font-size:12px;color:var(--ink-soft)}
.input svg{position:absolute;right:12px;top:13px}
.week-switch{position:absolute;left:214px;top:423px;display:flex;align-items:center;gap:8px;font-size:9.5px;color:var(--ink-soft)}
.week-switch .toggle{position:relative}
</style>
</head>
<body>
<div class="stage">

  <!-- Timers dashboard -->
  <section class="screen screen--timers">
    <header class="app-bar">
      <svg class="profile" width="14" height="16" viewBox="0 0 14 16"><circle cx="7" cy="4.5" r="3.5" fill="var(--icon)"/><path d="M0 16c0-4 3-6.5 7-6.5s7 2.5 7 6.5z" fill="var(--icon)"/></svg>
      <div class="brand">Velmaro</div>
      <svg class="wifi" width="18" height="14" viewBox="0 0 18 14"><path d="M1 5a12 12 0 0 1 16 0M4 8a7.5 7.5 0 0 1 10 0" fill="none" stroke="var(--icon)" stroke-width="2.2" stroke-linecap="round"/><circle cx="9" cy="11.5" r="2" fill="var(--icon)"/></svg>
      <svg class="menu" width="14" height="14" viewBox="0 0 14 14"><rect width="6" height="6" rx="1.5" fill="var(--icon)"/><rect x="8" width="6" height="6" rx="1.5" fill="var(--icon)"/><rect y="8" width="6" height="6" rx="1.5" fill="var(--icon)"/><rect x="8" y="8" width="6" height="6" rx="1.5" fill="var(--icon)"/></svg>
    </header>
    <h1 class="screen-title">Motorized sirens timers</h1>

    <div class="card shift-card">
      <svg class="icon" width="18" height="20" viewBox="0 0 18 20"><rect x="6" y="0" width="6" height="2.4" rx="1" fill="var(--primary)"/><circle cx="9" cy="11.5" r="7.2" fill="none" stroke="var(--primary)" stroke-width="2.2"/><path d="M9 11.5V7.5" stroke="var(--primary)" stroke-width="2.2" stroke-linecap="round"/></svg>
      <div class="name">Shift Timing</div>
      <div class="hint">Activate the device for shift timimg</div>
      <div class="toggle"><span class="track"></span><span class="knob"></span></div>
    </div>

    <div class="section-head">
      <svg width="15" height="15" viewBox="0 0 15 15"><rect x="0" y="2" width="15" height="13" rx="2" fill="var(--primary)"/><rect x="3" y="0" width="2" height="4" fill="var(--primary)"/><rect x="10" y="0" width="2" height="4" fill="var(--primary)"/><path d="M4.5 9.5l2 2 4-4" fill="none" stroke="#fff" stroke-width="1.6"/></svg>
      Schedules
    </div>

    <div class="card schedule" style="top:263px;height:116px">
      <div class="time">9:00 AM to 1:00 PM</div><div class="days">Weekdays</div>
      <div class="label">1st half session</div>
      <div class="audio">Audio: text to speech</div>
      <div class="note">The shift has been started, Have a nice day</div>
      <svg class="timer-icon" width="10" height="14" viewBox="0 0 10 14"><path d="M0 1h10M0 13h10M1 1c0 4 4 5 4 6s-4 2-4 6M9 1c0 4-4 5-4 6s4 2 4 6" fill="none" stroke="var(--icon)" stroke-width="1.6"/></svg>
      <svg class="edit-icon" width="13" height="13" viewBox="0 0 13 13"><path d="M0 13l.8-3.4L9.4 1a1.4 1.4 0 0 1 2 0l.6.6a1.4 1.4 0 0 1 0 2L3.4 12.2z" fill="var(--icon)"/></svg>
    </div>
    <div class="card schedule" style="top:395px;height:77px">
      <div class="time">1:00 PM to 2:00</div><div class="days">Weekdays</div>
      <div class="label">Lunch Time</div>
      <svg class="timer-icon" width="10" height="14" viewBox="0 0 10 14"><path d="M0 1h10M0 13h10M1 1c0 4 4 5 4 6s-4 2-4 6M9 1c0 4-4 5-4 6s4 2 4 6" fill="none" stroke="var(--icon)" stroke-width="1.6"/></svg>
      <svg class="edit-icon" width="13" height="13" viewBox="0 0 13 13"><path d="M0 13l.8-3.4L9.4 1a1.4 1.4 0 0 1 2 0l.6.6a1.4 1.4 0 0 1 0 2L3.4 12.2z" fill="var(--icon)"/></svg>
    </div>
    <div class="card schedule" style="top:487px;height:77px">
      <div class="time">4:00 PM to 4:20 PM</div><div class="days">Weekdays</div>
      <div class="label">Coffee Break</div>
      <svg class="timer-icon" width="10" height="14" viewBox="0 0 10 14"><path d="M0 1h10M0 13h10M1 1c0 4 4 5 4 6s-4 2-4 6M9 1c0 4-4 5-4 6s4 2 4 6" fill="none" stroke="var(--icon)" stroke-width="1.6"/></svg>
      <svg class="edit-icon" width="13" height="13" viewBox="0 0 13 13"><path d="M0 13l.8-3.4L9.4 1a1.4 1.4 0 0 1 2 0l.6.6a1.4 1.4 0 0 1 0 2L3.4 12.2z" fill="var(--icon)"/></svg>
    </div>
    <div class="card schedule" style="top:579px;height:77px">
      <div class="time">6:00 PM</div><div class="days">Weekdays</div>
      <div class="label">Signing out Time</div>
      <svg class="timer-icon" width="10" height="14" viewBox="0 0 10 14"><path d="M0 1h10M0 13h10M1 1c0 4 4 5 4 6s-4 2-4 6M9 1c0 4-4 5-4 6s4 2 4 6" fill="none" stroke="var(--icon)" stroke-width="1.6"/></svg>
      <svg class="edit-icon" width="13" height="13" viewBox="0 0 13 13"><path d="M0 13l.8-3.4L9.4 1a1.4 1.4 0 0 1 2 0l.6.6a1.4 1.4 0 0 1 0 2L3.4 12.2z" fill="var(--icon)"/></svg>
    </div>
    <div class="card schedule" style="top:671px;height:77px">
      <div class="time">9:00 AM to 12 PM</div><div class="days">Weekdays</div>
      <div class="label">Special Session</div>
      <svg class="timer-icon" width="10" height="14" viewBox="0 0 10 14"><path d="M0 1h10M0 13h10M1 1c0 4 4 5 4 6s-4 2-4 6M9 1c0 4-4 5-4 6s4 2 4 6" fill="none" stroke="var(--icon)" stroke-width="1.6"/></svg>
      <svg class="edit-icon" width="13" height="13" viewBox="0 0 13 13"><path d="M0 13l.8-3.4L9.4 1a1.4 1.4 0 0 1 2 0l.6.6a1.4 1.4 0 0 1 0 2L3.4 12.2z" fill="var(--icon)"/></svg>
    </div>

    <div class="status">
      <span class="dot"></span>
      <div class="head">Status</div>
      <div class="line">Next Ring of siren is at 1:00 PM to 2:00 PM which is lunch time</div>
      <div class="line">(Siren alarm in 2.0 mins)</div>
    </div>
  </section>

  <!-- Devices screen -->
  <section class="screen screen--devices">
    <header class="app-bar">
      <svg class="profile" width="14" height="16" viewBox="0 0 14 16"><circle cx="7" cy="4.5" r="3.5" fill="var(--icon)"/><path d="M0 16c0-4 3-6.5 7-6.5s7 2.5 7 6.5z" fill="var(--icon)"/></svg>
      <div class="brand">Velmaro</div>
      <svg class="wifi" width="18" height="14" viewBox="0 0 18 14"><path d="M1 5a12 12 0 0 1 16 0M4 8a7.5 7.5 0 0 1 10 0" fill="none" stroke="var(--icon)" stroke-width="2.2" stroke-linecap="round"/><circle cx="9" cy="11.5" r="2" fill="var(--icon)"/></svg>
      <svg class="menu" width="14" height="14" viewBox="0 0 14 14"><rect width="6" height="6" rx="1.5" fill="var(--icon)"/><rect x="8" width="6" height="6" rx="1.5" fill="var(--icon)"/><rect y="8" width="6" height="6" rx="1.5" fill="var(--icon)"/><rect x="8" y="8" width="6" height="6" rx="1.5" fill="var(--icon)"/></svg>
    </header>
    <h1 class="screen-title">Devices available to connect</h1>

    <div class="card device" style="top:123px">
      <svg class="icon" width="18" height="20" viewBox="0 0 18 20"><rect x="6" y="0" width="6" height="2.4" rx="1" fill="var(--primary)"/><circle cx="9" cy="11.5" r="7.2" fill="none" stroke="var(--primary)" stroke-width="2.2"/><path d="M9 11.5V7.5" stroke="var(--primary)" stroke-width="2.2" stroke-linecap="round"/></svg>
      <div class="name">XYZ timer</div>
      <div class="toggle"><span class="track"></span><span class="knob"></span></div>
    </div>
    <div class="card device" style="top:200px">
      <svg class="icon" width="20" height="18" viewBox="0 0 20 18"><path d="M0 6h4l6-5v16l-6-5H0z" fill="var(--primary)"/><path d="M13 5.5a5 5 0 0 1 0 7M15.5 3a8.5 8.5 0 0 1 0 12" fill="none" stroke="var(--primary)" stroke-width="1.8" stroke-linecap="round"/></svg>
      <div class="name">IT Siren abc</div>
      <div class="toggle"><span class="track"></span><span class="knob"></span></div>
    </div>
    <div class="card device" style="top:278px">
      <svg class="icon" width="20" height="20" viewBox="0 0 20 20"><path d="M3 10a7 7 0 0 1 14 0" fill="none" stroke="var(--primary)" stroke-width="2"/><rect x="1" y="9" width="4" height="7" rx="1.5" fill="var(--primary)"/><rect x="15" y="9" width="4" height="7" rx="1.5" fill="var(--primary)"/><ellipse cx="10" cy="11" rx="4.5" ry="6" fill="var(--primary)"/></svg>
      <div class="name">Support team speakers</div>
      <div class="toggle"><span class="track"></span><span class="knob"></span></div>
    </div>
  </section>

  <!-- New schedule form -->
  <section class="screen screen--schedule">
    <header class="app-bar">
      <svg class="profile" width="14" height="16" viewBox="0 0 14 16"><circle cx="7" cy="4.5" r="3.5" fill="var(--icon)"/><path d="M0 16c0-4 3-6.5 7-6.5s7 2.5 7 6.5z" fill="var(--icon)"/></svg>
      <div class="brand">Velmaro</div>
      <svg class="wifi" width="18" height="14" viewBox="0 0 18 14"><path d="M1 5a12 12 0 0 1 16 0M4 8a7.5 7.5 0 0 1 10 0" fill="none" stroke="var(--icon)" stroke-width="2.2" stroke-linecap="round"/><circle cx="9" cy="11.5" r="2" fill="var(--icon)"/></svg>
      <svg class="menu" width="14" height="14" viewBox="0 0 14 14"><rect width="6" height="6" rx="1.5" fill="var(--icon)"/><rect x="8" width="6" height="6" rx="1.5" fill="var(--icon)"/><rect y="8" width="6" height="6" rx="1.5" fill="var(--icon)"/><rect x="8" y="8" width="6" height="6" rx="1.5" fill="var(--icon)"/></svg>
    </header>
    <h1 class="screen-title">Add the new schedules for siren</h1>

    <div class="field-label" style="top:126px">Title of siren alarm</div>
    <div class="input" style="top:153px">Enter</div>

    <div class="field-label" style="top:215px">Start time of siren</div>
    <div class="input" style="top:242px">00:00</div>

    <div class="field-label" style="top:305px">End time of siren</div>
    <div class="input" style="top:332px">00:00</div>

    <div class="field-label" style="top:422px">Week</div>
    <div class="week-switch">
      <span>Weekday</span>
      <div class="toggle"><span class="track"></span><span class="knob"></span></div>
      <span>Weekend</span>
    </div>

    <div class="field-label" style="top:459px">Audio Format</div>
    <div class="input" style="top:486px">MP3 Audio
      <svg width="8" height="5" viewBox="0 0 8 5" style="top:16px"><path d="M.5.5L4 4 7.5.5" fill="none" stroke="var(--ink-soft)" stroke-width="1.1"/></svg>
    </div>

    <div class="field-label" style="top:555px">choose audio from files</div>
    <div class="field-label" style="top:588px">MP3 Audio</div>
    <div class="input" style="top:616px">Choose audio from files
      <svg width="11" height="11" viewBox="0 0 11 11"><path d="M5.5 0L2 3.5h2.2V7h2.6V3.5H9z" fill="var(--ink-soft)"/><rect x="0" y="8.5" width="11" height="2.5" fill="var(--ink-soft)"/></svg>
    </div>
  </section>

</div>
</body>
</html>
```